Half page (a5) ad for a company

I need a design for an ad for a company to be published in a conference catalogue. Please find enclosed the logo for a company. The company is providing health screening services. Ad should be subtle and minimalistic, i.e. logo in the centre and a phrase saying: "Be in charge of your own health" and the website bluefern.co.uk. Also please find enclosed guidlines for colours and fonts to be used.

```html
<!DOCTYPE html>
<html lang="en">
<head>
<meta charset="utf-8">
<title>Blue Fern Private — Be in charge of your own health</title>
<link rel="stylesheet" href="https://fonts.googleapis.com/css2?family=Montserrat:ital,wght@0,300;0,400;0,700;1,300&display=swap">
<style>
  :root {
    --ink-black: #040507;
    --paper-white: #ffffff;
    --soft-grey: #e4e4e6;
    --brand-red: #e5202a;
    --fruit-red: #c8141c;
    --fruit-deep: #5e0508;
  }
  html, body {
    margin: 0;
    padding: 0;
    width: 1200px;
    height: 846px;
    overflow: hidden;
    background: var(--ink-black);
  }
  .ad {
    position: relative;
    width: 1200px;
    height: 846px;
    background: var(--ink-black);
    font-family: "Montserrat", Arial, sans-serif;
    color: var(--paper-white);
  }
  .hero-photo {
    position: absolute;
    left: 430px;
    top: 240px;
    width: 320px;
    height: 260px;
    border-radius: 50% 50% 40% 40% / 45% 45% 55% 55%;
    background:
      radial-gradient(ellipse 55% 45% at 48% 35%, var(--fruit-red) 0%, #a10f15 45%, var(--fruit-deep) 75%, rgba(4,5,7,0) 100%);
  }
  .headline {
    position: absolute;
    left: 0;
    width: 1200px;
    top: 668px;
    margin: 0;
    text-align: center;
    font-size: 29px;
    letter-spacing: -0.8px;
    line-height: 1;
    font-weight: 700;
    transform: translateX(-9px);
  }
  .headline .emphasis {
    font-weight: 300;
    font-style: italic;
  }
  .website {
    position: absolute;
    left: 0;
    width: 1200px;
    top: 764px;
    margin: 0;
    text-align: center;
    font-size: 18px;
    font-weight: 300;
    letter-spacing: 4.2px;
    color: var(--soft-grey);
    transform: translateX(-10px);
  }
  .brand-name {
    position: absolute;
    left: 975px;
    width: 190px;
    top: 744px;
    margin: 0;
    text-align: center;
    font-size: 22px;
    font-weight: 400;
    line-height: 1.1;
    color: var(--brand-red);
  }
</style>
</head>
<body>
  <main class="ad">
    <div class="hero-photo" role="img" aria-label="Photograph of a glossy red apple with water droplets, lit from above against a black background"></div>
    <h1 class="headline">Be in charge of <span class="emphasis">your own health</span></h1>
    <p class="website">www.bluefern.co.uk.</p>
    <p class="brand-name">Blue Fern Private</p>
  </main>
</body>
</html>
```